Process Diagram - Circular Economy

I would like for a designer to take this rough sketch and turn it into a high quality design which can be used in a business presentation. Seeking to get both PDF and Jpeg file versions of the finished product.

Colours don't have to be the exact same as the rough sketch PDF, the green used is pretty ugly so open to some changes.

Target Market(s)

Corporate audience

Requirements
Must have
• Clear text for each party; VENOR, TORVIN, BUYER

Smaller text for the functions; marketing, recovery, logistics, cleaning, decontamination, testing & re-certification, storage, engineering suitability

```html
<!DOCTYPE html>
<html lang="en">
<head>
<meta charset="utf-8">
<title>Circular Economy Process Diagram</title>
<link href="https://fonts.googleapis.com/css2?family=Montserrat:wght@400;700;800&display=swap" rel="stylesheet">
<style>
  :root {
    --paper: #ffffff;
    --frame: #3a3a3a;
    --ink: #000000;
    --vendor-blue: #0070c0;
    --transit-grey: #6e6c6a;
    --process-orange: #ff6600;
    --storage-olive: #8a8f22;
    --newlife-green: #779a2f;
    --label-white: #ffffff;
  }
  html, body {
    margin: 0;
    padding: 0;
    width: 1200px;
    height: 1200px;
    overflow: hidden;
    background: var(--paper);
  }
  .diagram {
    display: block;
    width: 1200px;
    height: 1200px;
    font-family: "Montserrat", sans-serif;
  }
  .canvas-frame { fill: var(--paper); stroke: var(--frame); stroke-width: 3; }
  .process-ring { fill: none; stroke: var(--process-orange); stroke-width: 144; }
  .vendor-band { fill: url(#vendorFlow); }
  .storage-tail { fill: url(#storageFlow); }
  .marketing-strip { fill: var(--process-orange); }
  .newlife-arrow { fill: var(--newlife-green); }
  .stage-heading { fill: var(--ink); font-weight: 800; font-size: 64px; }
  .flow-label { fill: var(--label-white); font-weight: 400; font-size: 41px; }
  .party-name { font-weight: 700; }
  .stop-blue { stop-color: var(--vendor-blue); }
  .stop-grey { stop-color: var(--transit-grey); }
  .stop-orange { stop-color: var(--process-orange); }
  .stop-olive { stop-color: var(--storage-olive); }
</style>
</head>
<body>
<svg class="diagram" viewBox="0 0 1932 1932" xmlns="http://www.w3.org/2000/svg" role="img" aria-label="Circular economy process from end of life to new life">
  <defs>
    <linearGradient id="vendorFlow" gradientUnits="userSpaceOnUse" x1="260" y1="560" x2="1090" y2="890">
      <stop offset="0" class="stop-blue"/>
      <stop offset="0.5" class="stop-grey"/>
      <stop offset="1" class="stop-orange"/>
    </linearGradient>
    <linearGradient id="storageFlow" gradientUnits="userSpaceOnUse" x1="740" y1="800" x2="580" y2="930">
      <stop offset="0" class="stop-olive"/>
      <stop offset="0.85" class="stop-orange"/>
    </linearGradient>
    <path id="processRoute" d="M300,631 L929.6,799 A297,297 0 1 1 682.6,842.7"/>
  </defs>

  <rect class="canvas-frame" x="1.5" y="1.5" width="1929" height="1929"/>

  <!-- new life arrow -->
  <path class="newlife-arrow" d="M880,684 L1553,504 L1543,465 L1762,520 L1600,679 L1590,641 L1097,773 Q1010,705 880,684 Z"/>

  <!-- process loop: runs from under the vendor band round to under the storage tail -->
  <path class="process-ring" d="M933.2,787.6 A310,310 0 1 1 615.5,887.7"/>
  <path class="storage-tail" d="M522,895 A382,382 0 0 1 613,789 L833,847 A238,238 0 0 0 647,967 Z"/>

  <!-- end of life band, tangent to the loop -->
  <path class="vendor-band" d="M206,517 L951.9,718 A382,382 0 0 1 1183.8,896 L1059.1,968 A238,238 0 0 0 914.6,857.1 L169,655 L227,597 Z"/>
  <path class="marketing-strip" d="M447,682 L927.1,810.7 A286,286 0 0 1 1100.7,944 L1059.1,968 A238,238 0 0 0 914.6,857.1 L435,728.6 Z"/>

  <!-- headings -->
  <text class="stage-heading" transform="translate(255,510) rotate(15)">End of Life</text>
  <text class="stage-heading" transform="translate(1240,563) rotate(-15)">New Life</text>

  <!-- labels -->
  <text class="flow-label" textLength="2230" lengthAdjust="spacing">
    <textPath href="#processRoute" startOffset="15"><tspan class="party-name">VENDOR</tspan> - Recovery - Logistics - Cleaning <tspan class="party-name">- TORVIN -</tspan> Decontamination - Testing &amp; Re-certification - Storage</textPath>
  </text>
  <text class="flow-label" transform="translate(505,735) rotate(15)">Marketing</text>
  <text class="flow-label" transform="translate(1052,720) rotate(-15)">Engineering Suitability <tspan class="party-name">- BUYER</tspan></text>
</svg>
</body>
</html>
```